Flyer 2 Seiten Pflegestufe
Zielgruppe
Es handelt sich um einen mobilen Pflegedienst. Wir versorgen die Patienten ambulant in der Häuslichkeit. Im Mittelpunkt steht immer der Patient.

```html
<!DOCTYPE html>
<html lang="de">
<head>
<meta charset="utf-8">
<title>Pflegehaus Ostwind – Flyer</title>
<link rel="stylesheet" href="https://fonts.googleapis.com/css2?family=Source+Sans+3:ital,wght@0,400;0,600;0,700;1,400;1,600;1,700&display=swap">
<style>
  :root{
    --green:#5aae3a;
    --green-text:#4fa832;
    --orange:#f0911e;
    --purple:#3b2b8c;
    --ink:#3a3a3a;
    --panel:rgba(255,255,255,0.92);
  }
  *{box-sizing:border-box;margin:0;padding:0}
  html,body{width:1200px;height:856px;overflow:hidden}
  body{font-family:"Source Sans 3",Arial,sans-serif;color:var(--ink);background:#fff}
  .flyer{position:relative;width:1200px;height:856px;overflow:hidden}

  .backdrop{position:absolute;inset:0;
    background:
      radial-gradient(ellipse 420px 260px at 830px 420px,rgba(255,255,255,.95),rgba(255,255,255,0) 70%),
      radial-gradient(ellipse 380px 200px at 1010px 40px,rgba(255,255,255,.9),rgba(255,255,255,0) 70%),
      radial-gradient(ellipse 300px 360px at 120px 380px,rgba(200,208,214,.8),rgba(200,208,214,0) 75%),
      radial-gradient(ellipse 260px 200px at 600px 700px,rgba(214,220,224,.9),rgba(214,220,224,0) 75%),
      linear-gradient(180deg,#e7ecef 0%,#f3f5f6 40%,#dfe5e8 100%)}

  .heading{position:absolute;top:49px;height:70px;background:var(--green);border-radius:8px;
    color:#fff;font-weight:700;font-style:italic;font-size:33px;line-height:70px;white-space:nowrap}
  .heading--left{left:0;width:575px;padding-left:57px;border-radius:0 8px 8px 0}
  .heading--right{left:624px;width:576px;padding-left:34px;border-radius:8px 0 0 8px}

  .panel{position:absolute;background:var(--panel);border-radius:8px;box-shadow:0 2px 10px rgba(0,0,0,.07)}
  .panel--intro{left:32px;top:135px;width:543px;height:488px;padding:20px 0 0 25px}
  .panel--services{left:624px;top:135px;width:543px;height:583px;padding:20px 0 0 23px}

  .intro-lead{font-weight:700;font-style:italic;font-size:25.5px;line-height:33px;white-space:nowrap;margin-bottom:22px}
  .intro-text{font-size:26px;line-height:34.5px;white-space:nowrap;margin-bottom:22px}

  .services{list-style:none}
  .services li{position:relative;padding-left:26px;font-size:24.5px;line-height:34px;margin-bottom:21px;white-space:nowrap}
  .services li .tick{position:absolute;left:0;top:7px;width:20px;height:20px}
  .services em{color:var(--green-text);font-weight:600}
  .services-note{font-size:24.5px;line-height:33px;white-space:nowrap;margin-top:8px}

  .cta{position:absolute;left:624px;top:718px;width:543px;height:104px;background:var(--orange);
    border-radius:0 0 8px 8px;color:#fff;font-weight:700;font-style:italic;font-size:25px;line-height:36px;padding:12px 0 0 23px;white-space:nowrap}
  .cta .phone{display:inline-flex;align-items:center;gap:10px;margin-left:40px;font-style:normal;font-weight:700;font-size:29px;vertical-align:-1px}
  .cta .phone svg{width:27px;height:27px}

  .photo{position:absolute;left:-102px;top:643px;width:610px;height:610px;border-radius:50%;
    border:7px solid var(--purple);
    background:linear-gradient(120deg,#dfe3ea 0%,#efe9e2 30%,#b9c6d8 60%,#6f8ab8 100%)}

  .brand{position:absolute;left:392px;top:652px;width:150px;display:flex;flex-direction:column;align-items:center;gap:14px}
  .brand-dot{width:100px;height:100px;border-radius:50%;border:7px solid #2f6fb0;background:#fff}
  .brand-name{color:var(--green-text);font-weight:600;font-size:21px;line-height:24px;text-align:center}
</style>
</head>
<body>
<div class="flyer">
  <div class="backdrop" role="img" aria-label="Unscharfes Foto eines hellen Praxisflurs als Hintergrund"></div>

  <div class="heading heading--left">Ihr Pflegehaus-Ostwind in Rostock</div>
  <div class="heading heading--right">Wir unterstützen Sie gerne</div>

  <section class="panel panel--intro">
    <p class="intro-lead">Wenn ein hilfsbedürftiger Mensch und<br>dessen Angehörige in einer Pflegesituation<br>Hilfe benötigen, stellen sich viele Fragen:</p>
    <p class="intro-text">Wer unterstützt mich im Alltag? Wie kann<br>ich mein bisheriges Leben in vertrauter<br>Atmosphäre weiterleben? Wo bekomme ich<br>Hilfsmittel? Welche Anträge muss ich stellen?</p>
    <p class="intro-text">Auf diese und andere Fragen bekommen Sie<br>in Ihrem Pflegehaus-Ostwind eine Antwort.<br>Wir kümmern uns darum, dass Sie so lange<br>wie möglich in ihren eigenen vier Wänden<br>bleiben können.</p>
  </section>

  <section class="panel panel--services">
    <ul class="services">
      <li><svg class="tick" viewBox="0 0 22 22"><circle cx="11" cy="11" r="11" fill="#5aae3a"/><path d="M6 11.5l3.3 3.3L16 8" fill="none" stroke="#fff" stroke-width="2.6" stroke-linecap="round" stroke-linejoin="round"/></svg>Wir helfen Ihnen dabei, möglichst lange<br><em>im eigenen Zuhause verbleiben</em> zu können</li>
      <li><svg class="tick" viewBox="0 0 22 22"><circle cx="11" cy="11" r="11" fill="#5aae3a"/><path d="M6 11.5l3.3 3.3L16 8" fill="none" stroke="#fff" stroke-width="2.6" stroke-linecap="round" stroke-linejoin="round"/></svg>Wir unterstützen <em>kostenlos</em> bei der<br>Beantragung einer Pflegestufe</li>
      <li><svg class="tick" viewBox="0 0 22 22"><circle cx="11" cy="11" r="11" fill="#5aae3a"/><path d="M6 11.5l3.3 3.3L16 8" fill="none" stroke="#fff" stroke-width="2.6" stroke-linecap="round" stroke-linejoin="round"/></svg>Wir sorgen für die <em>Vernetzung</em> aller pflegeri-<br>schen, medizinischen und sozialen Leistungen</li>
      <li><svg class="tick" viewBox="0 0 22 22"><circle cx="11" cy="11" r="11" fill="#5aae3a"/><path d="M6 11.5l3.3 3.3L16 8" fill="none" stroke="#fff" stroke-width="2.6" stroke-linecap="round" stroke-linejoin="round"/></svg>Wir schaffen <em>Transparenz</em> für Betroffene<br>und Angehörige</li>
      <li><svg class="tick" viewBox="0 0 22 22"><circle cx="11" cy="11" r="11" fill="#5aae3a"/><path d="M6 11.5l3.3 3.3L16 8" fill="none" stroke="#fff" stroke-width="2.6" stroke-linecap="round" stroke-linejoin="round"/></svg><em>Wir unterstützen Menschen</em> in belastenden Si-<br>tuationen, auch durch psychosoziale Beratung</li>
    </ul>
    <p class="services-note">Im Pflegehaus Ostwind erhalten Sie indivi-<br>duelle und kostenfreie Beratung. Bei Bedarf<br>erfolgt die Beratung auch bei Ihnen zu Hause.</p>
  </section>

  <div class="cta">
    Rufen Sie uns kostenfrei an und vereinbaren<br>Sie einen Termin:<span class="phone"><svg viewBox="0 0 24 24"><path fill="#fff" d="M6.6 10.8a15.1 15.1 0 0 0 6.6 6.6l2.2-2.2a1 1 0 0 1 1-.25 11.4 11.4 0 0 0 3.6.57 1 1 0 0 1 1 1V20a1 1 0 0 1-1 1A17 17 0 0 1 3 4a1 1 0 0 1 1-1h3.5a1 1 0 0 1 1 1c0 1.25.2 2.45.57 3.57a1 1 0 0 1-.25 1z"/></svg>0800 44477 12</span>
  </div>

  <div class="photo" role="img" aria-label="Foto: ältere Frau und älterer Mann im Beratungsgespräch mit einer Pflegerin"></div>

  <div class="brand">
    <span class="brand-dot"></span>
    <span class="brand-name">Pflegehaus<br>Ostwind</span>
  </div>
</div>
</body>
</html>
```